Business Card Design Project

Cyber Security. Company name is brightHarbor.

Industry/Entity Type

Computer Security

Contact Information for Business Card

Gregory Lindqvist
Founder and Chief Hacker

2370 W. Alder Rd.
Suite 514
Chicago, IL 60482
773.555.0196
gregory.lindqvist@brightharbor.example
www.brightharbor.example

```html
<!DOCTYPE html>
<html lang="en">
<head>
<meta charset="utf-8">
<title>brightHarbor Business Card</title>
<link rel="stylesheet" href="https://fonts.googleapis.com/css2?family=Raleway:wght@400;500&display=swap">
<style>
  :root {
    --page-bg: #b9bcc4;
    --card-navy: #323646;
    --card-white: #ffffff;
    --ink: #1f1f24;
    --accent-blue: #5b6fc6;
    --mark-white: #ffffff;
    --rule: #2a2a2e;
  }
  * { margin: 0; padding: 0; box-sizing: border-box; }
  html, body {
    width: 1200px; height: 1200px; overflow: hidden;
    background: var(--page-bg);
    font-family: "Raleway", sans-serif;
  }
  .card {
    position: absolute;
    left: 170px;
    width: 860px; height: 491px;
    border-radius: 38px;
    box-shadow: 0 6px 14px rgba(0,0,0,0.18);
  }
  .card--front { top: 90px; background: var(--card-navy); }
  .card--back { top: 620px; background: var(--card-white); color: var(--ink); }

  .front-brand {
    position: absolute; left: 0; right: 0; top: 50%;
    transform: translateY(-50%);
    display: flex; align-items: center; justify-content: center; gap: 22px;
  }
  .front-brand__dot {
    width: 58px; height: 58px; border-radius: 50%;
    background: var(--accent-blue);
  }
  .front-brand__name {
    font-size: 66px; font-weight: 500; color: var(--mark-white);
    letter-spacing: 0.5px;
  }

  .holder { position: absolute; left: 64px; top: 150px; }
  .holder__name { font-size: 44px; font-weight: 500; line-height: 1; }
  .holder__surname { color: var(--accent-blue); }
  .holder__title { font-size: 21px; margin-top: 10px; }

  .divider {
    position: absolute; left: 64px; top: 262px;
    width: 610px; height: 2px; background: var(--rule);
  }
  .address { position: absolute; left: 64px; top: 282px; font-size: 18px; }

  .contacts {
    position: absolute; left: 64px; top: 338px;
    list-style: none; font-size: 21px;
  }
  .contacts__item { display: flex; align-items: center; gap: 18px; height: 38px; }
  .contacts__icon { width: 26px; height: 26px; flex: none; }

  .side-brand {
    position: absolute; right: 58px; top: 40px;
    display: flex; align-items: center; gap: 16px;
    transform-origin: top right;
    transform: rotate(90deg) translateX(100%);
  }
  .side-brand__dot {
    width: 44px; height: 44px; border-radius: 50%;
    background: var(--accent-blue);
  }
  .side-brand__name {
    font-size: 50px; font-weight: 500; color: var(--accent-blue);
  }
</style>
</head>
<body>
  <section class="card card--front">
    <div class="front-brand">
      <span class="front-brand__dot"></span>
      <span class="front-brand__name">brightHarbor</span>
    </div>
  </section>

  <section class="card card--back">
    <div class="side-brand">
      <span class="side-brand__dot"></span>
      <span class="side-brand__name">brightHarbor</span>
    </div>

    <div class="holder">
      <p class="holder__name">Gregory <span class="holder__surname">Lindqvist</span></p>
      <p class="holder__title">Founder and Chief Hacker</p>
    </div>

    <div class="divider"></div>

    <p class="address">2370 W. Alder Rd. Suite 514, Chicago, IL 60482</p>

    <ul class="contacts">
      <li class="contacts__item">
        <svg class="contacts__icon" viewBox="0 0 26 26" aria-hidden="true">
          <circle cx="13" cy="13" r="11" fill="none" stroke="#1f1f24" stroke-width="2"/>
          <path d="M9 8.5c0 5 3.5 8.5 8.5 8.5l1-2-2.5-1.2-1 1c-1.6-.6-2.9-1.9-3.5-3.5l1-1L11.3 7.5z" fill="#1f1f24"/>
        </svg>
        <span>773.555.0196</span>
      </li>
      <li class="contacts__item">
        <svg class="contacts__icon" viewBox="0 0 26 26" aria-hidden="true">
          <rect x="2" y="6" width="22" height="14" fill="none" stroke="#1f1f24" stroke-width="2"/>
          <path d="M2 6l11 8 11-8M2 20l8-7M24 20l-8-7" fill="none" stroke="#1f1f24" stroke-width="2"/>
        </svg>
        <span>gregory.lindqvist@brightharbor.example</span>
      </li>
      <li class="contacts__item">
        <svg class="contacts__icon" viewBox="0 0 26 26" aria-hidden="true">
          <g fill="none" stroke="#1f1f24" stroke-width="1.8">
            <circle cx="13" cy="13" r="11"/>
            <ellipse cx="13" cy="13" rx="5" ry="11"/>
            <path d="M2 13h22M4 7.5h18M4 18.5h18M13 2v22"/>
          </g>
        </svg>
        <span>www.brightharbor.example</span>
      </li>
    </ul>
  </section>
</body>
</html>
```